New Alcoholic Spiked Seltzer Line

We need a can design for a line of low calorie alcoholic seltzer. This product is a sparkling water and vodka drink with no sugar added in a slim 12 oz can.

This is a lighter, healthier, alternative to the sugary ready-to-drinks on the market. The product contains only 3 ingredients: Vodka, Water and Natural Flavors. It has only 100 calories but still has 5% alcohol, so you don't need to sacrifice alcohol to cut calories.

This product also does not contain any preservatives.

We want this design to communicate the following objectives to the consumer and in this order:

1. Appetizing product
2.Low calorie
3.Communicate the type of beverage (Spiked Seltzer)

The brand name of the product is VELKA.

The flavor of the product needed to be used for the design is Mango-Orange.

Comparable products are:

www.brisavelfizz.example/
https://www.tarnowbubble.example
https://quellrind.example/

The designs should not infringe or copy the creative directions of the products mentionned above. They are only given so that you can better understand the type of product we are developing.

Target Market(s)

Young Professional women between the ages of 25 and 44

Industry/Entity Type

Product

Colors

Designer to choose colors to be used in the design.

Requirements
Must have
• Design extendibility, meaning it can be adapted for other flavors.
• This is a new category in the market we are targeting, so consumers must easily be able to identify what type of product this is.

```html
<!DOCTYPE html>
<html lang="en">
<head>
<meta charset="utf-8">
<title>VELKA Spiked Seltzer — Can Labels</title>
<link href="https://fonts.googleapis.com/css2?family=Quicksand:wght@400;500;600&family=Great+Vibes&display=swap" rel="stylesheet">
<style>
  :root {
    --bg-top: #eef1f5;
    --bg-bottom: #c9ced6;
    --label-white: #fbfbfb;
    --label-shade: #e6e7e9;
    --mango-green: #a9c23a;
    --mango-gold: #d4a017;
    --mango-amber: #dc8f12;
    --orange-deep: #e0621e;
    --orange-mid: #d2691a;
    --orange-warm: #e38d1a;
    --tagline-grey: #8f9296;
    --flavour-ink: #f3f1ee;
  }
  html, body {
    margin: 0;
    padding: 0;
    width: 1200px;
    height: 1200px;
    overflow: hidden;
  }
  body {
    background: radial-gradient(circle at 35% 30%, var(--bg-top) 0%, var(--bg-bottom) 100%);
    font-family: "Quicksand", sans-serif;
  }
  .label-row {
    position: absolute;
    top: 170px;
    left: 0;
    width: 1200px;
    display: flex;
    justify-content: center;
    gap: 100px;
  }
  .can-label {
    width: 380px;
    height: 860px;
    box-shadow: 0 24px 40px rgba(60, 66, 76, 0.18);
  }
  .wordmark {
    font-family: "Quicksand", sans-serif;
    font-weight: 500;
    font-size: 128px;
    letter-spacing: 2px;
  }
  .wordmark--mango { fill: var(--mango-gold); }
  .wordmark--orange { fill: var(--orange-mid); }
  .tagline {
    font-family: "Quicksand", sans-serif;
    font-weight: 400;
    font-size: 26px;
    letter-spacing: 6px;
    fill: var(--tagline-grey);
  }
  .flavour-name {
    font-family: "Great Vibes", cursive;
    font-size: 64px;
    fill: var(--flavour-ink);
  }
  .can-size {
    font-family: "Quicksand", sans-serif;
    font-weight: 500;
    font-size: 18px;
    fill: var(--flavour-ink);
  }
  .badge-text {
    font-family: "Quicksand", sans-serif;
    font-weight: 600;
  }
  .badge-text--mango { fill: var(--mango-amber); }
  .badge-text--orange { fill: var(--orange-warm); }
  .bubble--mango { fill: var(--mango-amber); }
  .bubble-soft--mango { fill: var(--mango-green); }
  .bubble--orange { fill: var(--orange-warm); }
  .bubble-soft--orange { fill: var(--orange-deep); }
</style>
</head>
<body>
<main class="label-row">

  <!-- Mango flavour label -->
  <svg class="can-label" viewBox="0 0 380 860" xmlns="http://www.w3.org/2000/svg" aria-label="VELKA spiked seltzer, Mango, 12oz">
    <defs>
      <linearGradient id="label-sheen" x1="0" y1="0" x2="1" y2="0">
        <stop offset="0" stop-color="var(--label-shade)"/>
        <stop offset="0.35" stop-color="var(--label-white)"/>
        <stop offset="1" stop-color="var(--label-shade)"/>
      </linearGradient>
      <linearGradient id="band-mango" x1="0" y1="0" x2="1" y2="0">
        <stop offset="0" stop-color="var(--mango-green)"/>
        <stop offset="0.55" stop-color="var(--mango-gold)"/>
        <stop offset="1" stop-color="var(--mango-amber)"/>
      </linearGradient>
    </defs>
    <rect class="label-base" width="380" height="860" fill="url(#label-sheen)"/>

    <text class="wordmark wordmark--mango" transform="translate(205 335) rotate(-90)" text-anchor="middle">VELKA</text>
    <text class="tagline" transform="translate(282 365) rotate(-90)" text-anchor="middle">spiked seltzer</text>

    <g class="bubble-trail">
      <circle class="bubble--mango" cx="262" cy="172" r="13"/>
      <circle class="bubble--mango" cx="280" cy="150" r="6"/>
      <circle class="bubble--mango" cx="294" cy="164" r="5"/>
      <circle class="bubble--mango" cx="310" cy="150" r="4"/>
      <circle class="bubble--mango" cx="326" cy="136" r="4"/>
      <circle class="bubble--mango" cx="342" cy="118" r="3.5"/>
      <circle class="bubble--mango" cx="354" cy="96" r="3"/>
      <circle class="bubble--mango" cx="366" cy="70" r="2.5"/>
      <circle class="bubble-soft--mango" cx="40" cy="450" r="10"/>
      <circle class="bubble-soft--mango" cx="72" cy="430" r="9"/>
      <circle class="bubble-soft--mango" cx="50" cy="420" r="5"/>
      <circle class="bubble-soft--mango" cx="58" cy="398" r="4"/>
      <circle class="bubble-soft--mango" cx="78" cy="372" r="3"/>
      <circle class="bubble-soft--mango" cx="84" cy="352" r="2.5"/>
      <circle class="bubble-soft--mango" cx="40" cy="490" r="5"/>
      <circle cx="34" cy="545" r="7" fill="none" stroke="var(--mango-green)" stroke-width="2"/>
      <circle class="bubble-soft--mango" cx="24" cy="572" r="6"/>
    </g>

    <g class="badge">
      <circle cx="322" cy="548" r="38" fill="none" stroke="var(--mango-amber)" stroke-width="2"/>
      <text class="badge-text badge-text--mango" x="322" y="530" font-size="8" text-anchor="middle">LOW CARB</text>
      <text class="badge-text badge-text--mango" x="322" y="553" font-size="18" text-anchor="middle">5%</text>
      <text class="badge-text badge-text--mango" x="322" y="564" font-size="6" text-anchor="middle">ALCOHOL</text>
      <text class="badge-text badge-text--mango" x="322" y="574" font-size="6" text-anchor="middle">100 CALORIES</text>
    </g>

    <path class="flavour-band" d="M0 665 C90 650 140 650 210 630 C280 610 330 600 380 585 L380 860 L0 860 Z" fill="url(#band-mango)"/>
    <path class="flavour-band-edge" d="M0 665 C90 650 140 650 210 630 C280 610 330 600 380 585" fill="none" stroke="var(--label-white)" stroke-width="3"/>

    <ellipse class="fruit-art" role="img" aria-label="Mango illustration" cx="52" cy="625" rx="44" ry="30" fill="var(--mango-green)"/>

    <text class="flavour-name" x="185" y="740" text-anchor="middle">Mango</text>
    <text class="can-size" x="185" y="780" text-anchor="middle">12oz</text>
  </svg>

  <!-- Orange flavour label -->
  <svg class="can-label" viewBox="0 0 380 860" xmlns="http://www.w3.org/2000/svg" aria-label="VELKA spiked seltzer, Orange, 12oz">
    <defs>
      <linearGradient id="label-sheen-orange" x1="0" y1="0" x2="1" y2="0">
        <stop offset="0" stop-color="var(--label-shade)"/>
        <stop offset="0.35" stop-color="var(--label-white)"/>
        <stop offset="1" stop-color="var(--label-shade)"/>
      </linearGradient>
      <linearGradient id="band-orange" x1="0" y1="0" x2="1" y2="0">
        <stop offset="0" stop-color="var(--orange-deep)"/>
        <stop offset="0.55" stop-color="var(--orange-mid)"/>
        <stop offset="1" stop-color="var(--orange-warm)"/>
      </linearGradient>
    </defs>
    <rect class="label-base" width="380" height="860" fill="url(#label-sheen-orange)"/>

    <text class="wordmark wordmark--orange" transform="translate(205 335) rotate(-90)" text-anchor="middle">VELKA</text>
    <text class="tagline" transform="translate(282 365) rotate(-90)" text-anchor="middle">spiked seltzer</text>

    <g class="bubble-trail">
      <circle class="bubble--orange" cx="262" cy="172" r="13"/>
      <circle class="bubble--orange" cx="280" cy="150" r="6"/>
      <circle class="bubble--orange" cx="294" cy="164" r="5"/>
      <circle class="bubble--orange" cx="310" cy="150" r="4"/>
      <circle class="bubble--orange" cx="326" cy="136" r="4"/>
      <circle class="bubble--orange" cx="342" cy="118" r="3.5"/>
      <circle class="bubble--orange" cx="354" cy="96" r="3"/>
      <circle class="bubble--orange" cx="366" cy="70" r="2.5"/>
      <circle class="bubble-soft--orange" cx="40" cy="450" r="10"/>
      <circle class="bubble-soft--orange" cx="72" cy="430" r="9"/>
      <circle class="bubble-soft--orange" cx="50" cy="420" r="5"/>
      <circle class="bubble-soft--orange" cx="58" cy="398" r="4"/>
      <circle class="bubble-soft--orange" cx="78" cy="372" r="3"/>
      <circle class="bubble-soft--orange" cx="84" cy="352" r="2.5"/>
      <circle class="bubble-soft--orange" cx="40" cy="490" r="5"/>
      <circle cx="34" cy="545" r="7" fill="none" stroke="var(--orange-deep)" stroke-width="2"/>
      <circle class="bubble-soft--orange" cx="24" cy="572" r="6"/>
    </g>

    <g class="badge">
      <circle cx="322" cy="548" r="38" fill="none" stroke="var(--orange-warm)" stroke-width="2"/>
      <text class="badge-text badge-text--orange" x="322" y="530" font-size="8" text-anchor="middle">LOW CARB</text>
      <text class="badge-text badge-text--orange" x="322" y="553" font-size="18" text-anchor="middle">5%</text>
      <text class="badge-text badge-text--orange" x="322" y="564" font-size="6" text-anchor="middle">ALCOHOL</text>
      <text class="badge-text badge-text--orange" x="322" y="574" font-size="6" text-anchor="middle">100 CALORIES</text>
    </g>

    <path class="flavour-band" d="M0 665 C90 650 140 650 210 630 C280 610 330 600 380 585 L380 860 L0 860 Z" fill="url(#band-orange)"/>
    <path class="flavour-band-edge" d="M0 665 C90 650 140 650 210 630 C280 610 330 600 380 585" fill="none" stroke="var(--label-white)" stroke-width="3"/>

    <ellipse class="fruit-art" role="img" aria-label="Orange slice illustration" cx="52" cy="632" rx="44" ry="36" fill="var(--orange-deep)"/>

    <text class="flavour-name" x="185" y="740" text-anchor="middle">Orange</text>
    <text class="can-size" x="185" y="780" text-anchor="middle">12oz</text>
  </svg>

</main>
</body>
</html>
```